Business card design needed

We need a business card for a new business. We are called Tiny Toilers Gear, and we make replica kid size clothing, mainly hi vis shirts, work trousers and shorts. Our long term goal is to include clothing for numerous trades and professions, for our littlest Aussies. We would like a kid friendly card using navy blue, bright orange, bright yellow and bright pink. We haven't set up our web page yet because we want to base it on our final business card design.
Updates

Industry/Entity Type

Clothing

```html
<!DOCTYPE html>
<html lang="en">
<head>
<meta charset="utf-8">
<title>Tiny Toilers Gear – Business Card</title>
<link rel="stylesheet" href="https://fonts.googleapis.com/css2?family=Dancing+Script:wght@500;700&display=swap">
<style>
  :root {
    --page: #ffffff;
    --sky: #a0d8f4;
    --fold-grey: #dcdddd;
    --curl-pink: #e3007f;
    --brand-pink: #e3007f;
    --ink: #2b2b2b;
    --navy-blue: #008bd6;
    --sun-yellow: #fdec00;
    --amber: #fbd000;
    --lime: #abcd22;
    --grass: #009a4c;
  }
  html, body {
    margin: 0;
    padding: 0;
    width: 1200px;
    height: 900px;
    overflow: hidden;
    background: var(--page);
  }
  .business-card {
    position: absolute;
    left: 0;
    top: 112px;
    width: 1200px;
    height: 676px;
    display: block;
  }
  .brand-name {
    font-family: "Dancing Script", cursive;
    font-weight: 700;
    font-size: 92px;
    fill: var(--brand-pink);
  }
  .contact-label {
    font-family: "Dancing Script", cursive;
    font-weight: 500;
    font-size: 50px;
    fill: var(--ink);
  }
  .panel-sky { fill: var(--sky); }
  .corner-fold { fill: var(--fold-grey); }
  .page-curl { fill: var(--curl-pink); }
  .tri-blue { fill: var(--navy-blue); }
  .tri-yellow { fill: var(--sun-yellow); }
  .tri-amber { fill: var(--amber); }
  .tri-lime { fill: var(--lime); }
  .tri-green { fill: var(--grass); }
</style>
</head>
<body>
  <svg class="business-card" viewBox="0 0 1340 755" preserveAspectRatio="none" xmlns="http://www.w3.org/2000/svg">
    <defs>
      <path id="brand-arc" d="M380,140 Q720,250 1190,500"/>
    </defs>

    <rect class="panel-sky" x="0" y="0" width="840" height="755"/>
    <path class="corner-fold" d="M0,0 L343,0 L100,165 C40,205 0,260 0,330 Z"/>
    <path class="page-curl" d="M343,0 L100,165 C40,205 0,260 0,330 C10,200 110,180 203,302 C230,200 280,80 343,0 Z"/>

    <g class="geometric-panel">
      <polygon class="tri-blue" points="838,0 1340,0 1340,205"/>
      <polygon class="tri-yellow" points="838,0 1340,205 838,537"/>
      <polygon class="tri-amber" points="1340,205 1340,755 838,537"/>
      <polygon class="tri-lime" points="838,537 1340,755 838,755"/>
      <polygon class="tri-green" points="838,537 838,755 741,755"/>
    </g>

    <text class="brand-name"><textPath href="#brand-arc">Tiny Toilers Gear</textPath></text>

    <g class="contact-details">
      <text class="contact-label" x="80" y="400">Address</text>
      <text class="contact-label" x="80" y="482">Web</text>
      <text class="contact-label" x="80" y="566">Email</text>
      <text class="contact-label" x="80" y="648">Product</text>
    </g>
  </svg>
</body>
</html>
```